Business Card Design

I am a cosmetic tattooist in Melbourne Australia, who provides services where by I tattoo eyebrows in block or strokes with a tattooing gun. Feathering that mimic hair strands with a scalpel. Eyeliner top and bottom with the tattooing gun. Lips just as either an outline or a full block colour where the top and bottom lip is completely covered. Corrections for tattooing done previously that have either faded to quickly, turned blue or orange due to bad colour choice, or a mishap. Paramedical colouring for people who either have scaring that needs to be matched to their skin colour. Patients who have alopecia or a skin condition that needs hair like tattooing. Cancer patients who's nipples and areolas have been partially or totally been removed and require them to be re drawn into the new skin. I colour match with a variety of inks (around 50) at my disposal and can also lift colours with a pigmentation lifter. I also require the use of two different types of anaesthetics throughout each procedure.
Colours that I have looked into the represent health, professionalism, beauty, skin and medical type procedures are Light to dark brown, Light to dark grey, Black and White. Possibly a splash of red to represent the lips. I am mobile and can work from any venue that takes a commission for a bed. I have completed a diploma in cosmetic tattooing being qualified.
Updates

Project Deadline Extended
Reason: I have been awaiting for a design from own more designer who accepted my project but hasn't released their design.

Project Deadline Extended

Industry/Entity Type

Medical

Contact Information for Business Card

Company name: Velora Cosmetic Tattooing
Name: Joanne Pilbury
Title: Cosmetic and Paramedical Tattooist
Address: P.O Box 2863, Ashcombe Rise, Victoria 3187
Mobile: 0417385926
Email: veloracosmetictattooing@examplemail.net
Preferred colours: Light brown, Light Grey, Black (writing) White Background

Requirements
Nice to have
• A shape of the eyebrow or eye with eyeliner in the background. Possibly red lips. No straight lines, only curved or curled lines.

```html
<!DOCTYPE html>
<html lang="en">
<head>
<meta charset="utf-8">
<title>Velora Cosmetic Tattooing – Business Card</title>
<link rel="stylesheet" href="https://fonts.googleapis.com/css2?family=Abril+Fatface&family=Arimo&family=Open+Sans:wght@400&display=swap">
<style>
  :root {
    --paper: #ffffff;
    --ink: #111111;
    --skin-light: #f4d3c4;
    --skin-mid: #e9a58e;
    --skin-deep: #d8735c;
    --lash-shadow: #9a6a5c;
  }
  html, body {
    margin: 0;
    padding: 0;
    overflow: hidden;
    background: var(--paper);
  }
  .card {
    position: relative;
    width: 1200px;
    height: 741px;
    overflow: hidden;
    background: var(--paper);
  }
  .card__artwork {
    position: absolute;
    inset: 0;
    width: 1200px;
    height: 741px;
  }
  .card__text {
    position: absolute;
    margin: 0;
    color: var(--ink);
    white-space: nowrap;
    line-height: 1;
  }
  .company-name {
    left: 0;
    width: 1226px;
    top: 58px;
    text-align: center;
    font-family: "Abril Fatface", serif;
    font-size: 78px;
    line-height: 80px;
    font-weight: 400;
    letter-spacing: 0.5px;
  }
  .postal-address {
    left: 0;
    width: 1226px;
    top: 244px;
    text-align: center;
    font-family: "Arimo", sans-serif;
    font-size: 35px;
  }
  .contact-block {
    position: absolute;
    right: 79px;
    top: 370px;
    text-align: right;
    color: var(--ink);
  }
  .person-name {
    margin: 0;
    font-family: "Open Sans", sans-serif;
    font-weight: 400;
    font-size: 86px;
    line-height: 90px;
    letter-spacing: 1px;
  }
  .person-role,
  .person-phone,
  .person-email {
    margin: 0;
    font-family: "Arimo", sans-serif;
    font-size: 35px;
    line-height: 43px;
  }
  .person-role { margin-top: 20px; }
  .person-phone { margin-top: 14px; }
</style>
</head>
<body>
<main class="card">
  <svg class="card__artwork" viewBox="0 0 1200 741" role="img" aria-label="Close-up photograph of a woman's eye with tattooed eyeliner, long lashes and a shaped eyebrow">
    <defs>
      <radialGradient id="skinGlow" cx="230" cy="560" r="700" gradientUnits="userSpaceOnUse">
        <stop offset="0" stop-color="var(--skin-deep)"/>
        <stop offset="0.35" stop-color="var(--skin-mid)"/>
        <stop offset="0.62" stop-color="var(--skin-light)"/>
        <stop offset="0.85" stop-color="var(--paper)"/>
      </radialGradient>
      <radialGradient id="lidShade" cx="200" cy="610" r="260" gradientUnits="userSpaceOnUse">
        <stop offset="0" stop-color="var(--lash-shadow)" stop-opacity="0.55"/>
        <stop offset="1" stop-color="var(--lash-shadow)" stop-opacity="0"/>
      </radialGradient>
      <linearGradient id="topFade" x1="0" y1="0" x2="0" y2="1">
        <stop offset="0.25" stop-color="var(--paper)"/>
        <stop offset="0.45" stop-color="var(--paper)" stop-opacity="0"/>
      </linearGradient>
    </defs>
    <rect width="1200" height="741" fill="url(#skinGlow)"/>
    <rect width="1200" height="741" fill="url(#lidShade)"/>
    <rect width="1200" height="741" fill="url(#topFade)"/>
  </svg>

  <h1 class="card__text company-name">Velora Cosmetic<br>Tattooing</h1>
  <p class="card__text postal-address">P.O Box 2863, Ashcombe Rise, Victoria 3187</p>

  <section class="contact-block">
    <h2 class="person-name">JOANNE PILBURY</h2>
    <p class="person-role">Cosmetic and<br>Paramedical Tattooist</p>
    <p class="person-phone">0417385926</p>
    <p class="person-email">veloracosmetictattooing@examplemail.net</p>
  </section>
</main>
</body>
</html>
```